Office Stationary and Business Card package

I need a new fresh looking business card and stationary design. "I need to refresh and update my Stationary and Business card appearance.

We are a family dental practice that handles all phases of dentistry including cosmetic, emergency and implant restoration We like the use of Blue and Grey in the design. i would like to include my website address and Phone numbers on the new project as well as a choice of different back sides to business cards which might include a map, appointment information, or blank depending on the particular card. The business cards should allow for the inclusion of another persons name and title in some location.

Information to be included in stationery:

Gordon T Malvey DMD, FAIDS
A Professional Dental Corporation (this needs to be
somewhere on the stationary and business cards)
48160 Orchard Lane
Larkmont, CA 90811
PHONE: (555) 317-4092
WEBSITE: www.gordonmalveydmd.example

Designs need to be Vibrant, Professional and Clean.
Colors to use: Blue, Grey and White colors.

I currently do not have an existing logo. I would like something simply, similar to the attached.

```html
<!DOCTYPE html>
<html lang="en">
<head>
<meta charset="utf-8">
<title>Gordon T Malvey DMD, FAIDS — Business Card</title>
<link rel="stylesheet" href="https://fonts.googleapis.com/css2?family=Signika:wght@600&family=Share+Tech+Mono&display=swap">
<style>
  :root {
    --page: #ffffff;
    --slate: #202a33;
    --cyan: #039dcd;
    --ink: #1c2630;
    --white: #ffffff;
  }
  * { margin: 0; padding: 0; box-sizing: border-box; }
  html, body {
    width: 1200px;
    height: 1200px;
    overflow: hidden;
    background: var(--page);
  }
  .card {
    position: absolute;
    left: 12px;
    top: 418px;
    width: 1175px;
    height: 368px;
    display: flex;
  }
  .card-front {
    width: 587px;
    height: 100%;
    background: var(--slate);
    position: relative;
  }
  .card-back {
    flex: 1;
    height: 100%;
    background: var(--cyan);
    position: relative;
  }
  .brand {
    position: absolute;
    left: 0;
    right: 0;
    top: 106px;
    text-align: center;
  }
  .brand-mark {
    display: block;
    width: 72px;
    height: 72px;
    margin: 0 auto 14px;
    border-radius: 50%;
    background: var(--cyan);
  }
  .brand-name {
    font-family: "Signika", sans-serif;
    font-weight: 600;
    font-size: 32px;
    letter-spacing: -0.6px;
    color: var(--cyan);
    line-height: 1;
    white-space: nowrap;
  }
  .brand-tagline {
    margin-top: 9px;
    font-family: "Share Tech Mono", monospace;
    font-variant: small-caps;
    font-size: 18px;
    letter-spacing: 3.4px;
    color: var(--white);
    white-space: nowrap;
  }
  .contact {
    position: absolute;
    left: 137px;
    top: 124px;
    list-style: none;
    font-family: "Share Tech Mono", monospace;
    font-variant: small-caps;
    font-size: 22px;
    letter-spacing: 4px;
    color: var(--ink);
  }
  .contact-item {
    display: flex;
    align-items: flex-start;
    margin-bottom: 10px;
    line-height: 26px;
    white-space: nowrap;
  }
  .contact-item.web { font-size: 18px; letter-spacing: 4px; }
  .contact-icon {
    width: 22px;
    height: 26px;
    margin-right: 18px;
    flex: none;
  }
</style>
</head>
<body>
  <div class="card">
    <section class="card-front">
      <div class="brand">
        <span class="brand-mark"></span>
        <div class="brand-name">Gordon T Malvey DMD, FAIDS</div>
        <div class="brand-tagline">A Professional Dental Corporation</div>
      </div>
    </section>
    <section class="card-back">
      <ul class="contact">
        <li class="contact-item">
          <svg class="contact-icon" viewBox="0 0 22 26" fill="none" stroke="#ffffff" stroke-width="1.4">
            <path d="M11 24 C5 16 3 12.5 3 9.5 A8 8 0 0 1 19 9.5 C19 12.5 17 16 11 24 Z"/>
            <circle cx="11" cy="9.5" r="3.2"/>
          </svg>
          <span>48160 Orchard Lane<br>Larkmont, CA 90811</span>
        </li>
        <li class="contact-item">
          <svg class="contact-icon" viewBox="0 0 22 26" fill="none" stroke="#ffffff" stroke-width="1.4">
            <rect x="5" y="1" width="12" height="24" rx="1.5"/>
            <line x1="5" y1="4.5" x2="17" y2="4.5"/>
            <line x1="5" y1="21" x2="17" y2="21"/>
            <circle cx="11" cy="23" r="0.6"/>
          </svg>
          <span>(555) 317-4092</span>
        </li>
        <li class="contact-item web">
          <svg class="contact-icon" viewBox="0 0 22 26" fill="none" stroke="#ffffff" stroke-width="1.3">
            <circle cx="11" cy="13" r="9"/>
            <ellipse cx="11" cy="13" rx="4" ry="9"/>
            <line x1="2" y1="13" x2="20" y2="13"/>
            <path d="M3.5 8.5 H18.5 M3.5 17.5 H18.5"/>
          </svg>
          <span>www.gordonmalveydmd.example</span>
        </li>
      </ul>
    </section>
  </div>
</body>
</html>
```